Business Card Design Needed

Business car design required, logo will be supplied.

Brackenfield Heat Surveyors are looking to become the leading provider of energy performance certificates to estate agents, landlords and home owners in the Yorkshire region of the UK.

The business card must be double sided and professional looking. Estate agents receive hundreds of cards from contractors and our card must stand out.

I require a two sided business card that is clean, modern and created by a designer that can think outside of the box.

Brand colours can be supplied .

Please ask if you have any questions.

Target Market(s)

Estate agents, landlords and property owners

Industry/Entity Type

Property - estate agency - energy consultants

Contact Information for Business Card

Tomas Birchwell - Energy Assessor - 07351642170 - www.BrackenfieldHSV.co.uk - info@brackenfieldhsv.co.uk

Font styles to use
Serif
Sans Serif

Colors
00AB8E
00BBA5
67D7C9
C6EFE9
E9F9F6

Requirements
Must have
• Use the provided logo, clean, professional and stand out from the crowd
Nice to have
• Clever use of text, spacing and brand colours
Should not have
• Clip art

```html
<!DOCTYPE html>
<html lang="en">
<head>
<meta charset="utf-8">
<title>Brackenfield Heat Surveyors – Business Card</title>
<link href="https://fonts.googleapis.com/css2?family=Arimo:wght@400;700&display=swap" rel="stylesheet">
<style>
  :root{
    --brand-blue:#1d6fb1;
    --brand-blue-dark:#155a94;
    --brand-blue-light:#2a86c9;
    --brand-green:#a9c92b;
    --ink:#222629;
    --paper:#ffffff;
    --backdrop:#c9c9c9;
  }
  *{box-sizing:border-box;margin:0;padding:0}
  html,body{width:1200px;height:788px;overflow:hidden}
  body{
    background:linear-gradient(180deg,#d4d4d4 0%,var(--backdrop) 55%,#b9b9b9 100%);
    font-family:"Arimo",Arial,sans-serif;
    position:relative;
  }
  .card{
    position:absolute;
    width:560px;height:320px;
    border-radius:22px;
    overflow:hidden;
    box-shadow:0 14px 30px rgba(0,0,0,.22);
  }
  /* ---------- front ---------- */
  .card--front{left:90px;top:56px;background:var(--paper)}
  .card--front .edge-band{
    position:absolute;left:0;right:0;bottom:0;height:10px;display:flex
  }
  .edge-band .edge-blue{flex:0 0 56%;background:var(--brand-blue)}
  .edge-band .edge-green{flex:1;background:var(--brand-green)}

  .brand-lockup{
    position:absolute;display:flex;align-items:center;gap:12px;
  }
  .card--front .brand-lockup{left:196px;top:50px}
  .brand-mark{width:38px;height:38px;border-radius:50%;border:4px solid var(--brand-blue);flex:none}
  .brand-divider{width:1px;height:44px;background:var(--brand-blue)}
  .brand-name{
    font-size:19px;font-weight:400;color:var(--brand-blue);
    line-height:1.15;letter-spacing:.02em;width:150px
  }

  .person{position:absolute;left:34px;top:168px}
  .person-name{
    font-size:27px;font-weight:700;letter-spacing:.01em;text-transform:uppercase;line-height:1
  }
  .person-name .first{color:var(--brand-blue)}
  .person-name .last{color:var(--brand-green)}
  .person-role{font-size:17px;color:var(--ink);margin-top:6px}

  .rule{position:absolute;left:34px;right:0;top:236px;height:1px;background:var(--brand-green)}

  .contact-list{position:absolute;left:34px;top:250px;list-style:none}
  .contact-list li{display:flex;align-items:center;gap:8px;font-size:16px;color:var(--ink);line-height:23px}
  .contact-list svg{width:13px;height:13px;flex:none;fill:var(--brand-blue)}
  .web{
    position:absolute;right:26px;top:250px;display:flex;align-items:center;gap:7px;
    font-size:14px;color:var(--ink);line-height:23px
  }
  .web svg{width:12px;height:12px;fill:var(--brand-blue)}

  /* ---------- back ---------- */
  .card--back{left:550px;top:412px}
  .back-field{
    position:absolute;inset:0;
    background:radial-gradient(circle at 85% 10%,var(--brand-blue-light) 0%,var(--brand-blue) 45%,var(--brand-blue-dark) 100%);
  }
  .card--back .brand-lockup{right:34px;bottom:52px}
  .card--back .brand-mark{border-color:var(--paper)}
  .card--back .brand-divider{background:var(--paper)}
  .card--back .brand-name{color:var(--paper)}
</style>
</head>
<body>

  <section class="card card--front" aria-label="Business card front">
    <div class="brand-lockup">
      <span class="brand-mark"></span>
      <span class="brand-divider"></span>
      <span class="brand-name">Brackenfield Heat Surveyors</span>
    </div>

    <div class="person">
      <p class="person-name"><span class="first">Tomas</span> <span class="last">Birchwell</span></p>
      <p class="person-role">Energy Assessor</p>
    </div>

    <div class="rule"></div>

    <ul class="contact-list">
      <li>
        <svg viewBox="0 0 24 24" aria-hidden="true"><path d="M6.6 10.8a15 15 0 0 0 6.6 6.6l2.2-2.2c.3-.3.7-.4 1-.2 1.1.4 2.3.6 3.6.6.6 0 1 .4 1 1V20c0 .6-.4 1-1 1A17 17 0 0 1 3 4c0-.6.4-1 1-1h3.5c.6 0 1 .4 1 1 0 1.3.2 2.5.6 3.6.1.3 0 .7-.2 1z"/></svg>
        07351642170
      </li>
      <li>
        <svg viewBox="0 0 24 24" aria-hidden="true"><path d="M2 5h20v14H2z M2 5l10 8 10-8" fill="none" stroke="#1d6fb1" stroke-width="2.4"/></svg>
        info@brackenfieldhsv.co.uk
      </li>
    </ul>

    <div class="web">
      <svg viewBox="0 0 24 24" aria-hidden="true"><circle cx="12" cy="12" r="11"/></svg>
      www.BrackenfieldHSV.co.uk
    </div>

    <div class="edge-band"><span class="edge-blue"></span><span class="edge-green"></span></div>
  </section>

  <section class="card card--back" aria-label="Business card back">
    <div class="back-field" role="img" aria-label="Blue background with a repeating brand-mark pattern"></div>
    <div class="brand-lockup">
      <span class="brand-mark"></span>
      <span class="brand-divider"></span>
      <span class="brand-name">Brackenfield Heat Surveyors</span>
    </div>
  </section>

</body>
</html>
```